digger and truck hire

this is a new business - Digger and Truck
we would like to include the attached photo of the digger and truck - as the truck is red and the digger is green
maybe either black or white lettering which ever suits

Industry/Entity Type

Business

Contact Information for Business Card

RDL - Ruddas 2.5t Mini Digger and 7t Tip Truck -Hire, full attachments, augers, trenching, site preparation, small aggregate deliveries
Phone 0218365914
rudda.rdl@plinto.co.nz

```html
<!DOCTYPE html>
<html lang="en">
<head>
<meta charset="utf-8">
<title>RDL - Ruddas Business Card</title>
<link rel="stylesheet" href="https://fonts.googleapis.com/css2?family=Quicksand:wght@400;500;600&display=swap">
<style>
  :root {
    --page-bg: #e9e7e4;
    --card-bg: #ffffff;
    --teal: #0fa497;
    --teal-dark: #3d7d76;
    --ink: #3a3a3a;
    --service-ink: #111717;
    --contact-green: #2a9a5a;
  }
  * { margin: 0; padding: 0; box-sizing: border-box; }
  html, body {
    width: 1200px; height: 900px; overflow: hidden;
    background: var(--page-bg);
    font-family: "Quicksand", sans-serif;
  }
  .business-card {
    position: absolute; left: 120px; top: 156px;
    width: 960px; height: 588px;
    background: var(--card-bg);
    overflow: hidden;
    box-shadow: 0 6px 24px rgba(0,0,0,.18);
  }
  .stripe-stack {
    position: absolute; left: -220px; top: 217px; width: 1400px;
    display: flex; flex-direction: column; gap: 10px;
    transform: rotate(-18.4deg);
    transform-origin: 700px 77px;
  }
  .band { background: var(--teal); padding-left: 420px; }
  .band-thin { height: 22px; }
  .band-main { padding-top: 10px; padding-bottom: 10px; }
  .band-last { padding-top: 8px; padding-bottom: 10px; }
  .service-line {
    font-size: 30px; line-height: 38px; font-weight: 600;
    color: var(--service-ink); white-space: nowrap;
  }
  .machinery-art {
    position: absolute; left: 640px; top: 30px;
    width: 240px; height: 170px;
    background: linear-gradient(135deg, rgba(61,125,118,.45), rgba(61,125,118,.8));
    border-radius: 8px;
  }
  .brand-block {
    position: absolute; left: 300px; top: 70px; width: 360px;
    text-align: center;
  }
  .brand-name {
    font-size: 46px; font-weight: 400; color: var(--ink);
    letter-spacing: 1px; line-height: 1.1;
  }
  .contact-line {
    display: flex; align-items: center; justify-content: center;
    gap: 10px; margin-top: 8px;
  }
  .contact-line svg { width: 26px; height: 26px; fill: var(--teal); flex: none; }
  .contact-phone { font-size: 26px; color: var(--contact-green); font-weight: 500; }
  .contact-email { font-size: 18px; color: var(--ink); }
</style>
</head>
<body>
  <div class="business-card">
    <div class="stripe-stack">
      <div class="band band-thin" aria-hidden="true"></div>
      <div class="band band-main">
        <p class="service-line">2.5t Mini Digger</p>
        <p class="service-line">7t Tip Truck</p>
        <p class="service-line">Hire, full attachments, augers, trenching,</p>
      </div>
      <div class="band band-last">
        <p class="service-line">site preparation, small aggregate deliveries</p>
      </div>
    </div>

    <div class="machinery-art" role="img" aria-label="Illustration of a backhoe digger"></div>

    <div class="brand-block">
      <div class="brand-name">RDL - Ruddas</div>
      <div class="contact-line">
        <svg viewBox="0 0 24 24" aria-hidden="true"><path d="M4 9c0-2 3-4 8-4s8 2 8 4v2h-4V9.5c-1-.6-2.3-.9-4-.9s-3 .3-4 .9V11H4zM7 12h10l2 7H5z"/></svg>
        <span class="contact-phone">0218365914</span>
      </div>
      <div class="contact-line">
        <svg viewBox="0 0 24 24" aria-hidden="true"><path d="M12 2a10 10 0 1 0 0 20 10 10 0 0 0 0-20zm6.9 9h-3a15 15 0 0 0-1.2-5.6A8 8 0 0 1 18.9 11zM12 4c.9 1.2 1.8 3.6 1.9 7h-3.8c.1-3.4 1-5.8 1.9-7zM9.3 5.4A15 15 0 0 0 8.1 11h-3a8 8 0 0 1 4.2-5.6zM5.1 13h3a15 15 0 0 0 1.2 5.6A8 8 0 0 1 5.1 13zM12 20c-.9-1.2-1.8-3.6-1.9-7h3.8c-.1 3.4-1 5.8-1.9 7zm2.7-1.4a15 15 0 0 0 1.2-5.6h3a8 8 0 0 1-4.2 5.6z"/></svg>
        <span class="contact-email">rudda.rdl@plinto.co.nz</span>
      </div>
    </div>
  </div>
</body>
</html>
```